social interest sharing site needs a web site design

we need a web site design for a social web platform.
the site is one page(main page), that is split into 3 sections
each section is a different color(red,green and blue)
and a user can choose to share each of the sections.
any section/color will contain boxes , each box can contain different media types.

the media types:
* list of URLS
* list of articles including title + image + description
* list of videos
* thumbnails of images
* calender
* list of emails

the main content will look like corkboardly layout
multiple boxes each box can contain different type of content as described above

each color is a different tab
each tab will have layout like corkboardly
Updates

please read the last description update.
and i uploaded an image that can explain the requirements better

thanks
Oren
 

Industry/Entity Type

Media

```html
<!DOCTYPE html>
<html lang="en">
<head>
<meta charset="utf-8">
<title>Noticely.me – My Home Page</title>
<link href="https://fonts.googleapis.com/css2?family=Open+Sans:wght@400;600;700&display=swap" rel="stylesheet">
<style>
:root{
  --red:#9b140a;
  --green:#5fae23;
  --blue:#0d3a70;
  --navy-btn:#0a3a6e;
  --ink:#111;
  --grey:#7a7a7a;
  --light-grey:#8a8a8a;
  --white:#fff;
  --post-blue:#3b7fc4;
  --chirp-blue:#13a3e6;
}
*{box-sizing:border-box;margin:0;padding:0}
html,body{width:1200px;height:782px;overflow:hidden;background:var(--white);font-family:"Open Sans",sans-serif}
.canvas{position:relative;width:1200px;height:782px}
.brand{position:absolute;left:70px;top:30px;font-size:27px;font-weight:700;color:var(--ink);letter-spacing:-1px;font-family:"Open Sans",sans-serif}
.main-nav a{position:absolute;top:0;height:70px;line-height:97px;font-size:14px;font-weight:600;letter-spacing:1px;text-decoration:none;font-family:"Open Sans",sans-serif}
.nav-home{left:248px;width:138px;background:var(--red);color:var(--white);text-align:center}
.nav-videos{left:401px;color:var(--green)}
.nav-apps{left:590px;color:var(--red)}
.top-links{position:absolute;top:9px;right:70px;display:flex;align-items:center;gap:8px;font-size:10px;color:var(--light-grey)}
.top-links .dot{width:8px;height:8px;border-radius:50%;background:#9a9a9a}
.quick-links{position:absolute;top:34px;left:835px;display:flex;gap:2px}
.quick-links a{display:block;height:32px;padding:5px 9px;background:var(--navy-btn);color:var(--white);font-size:9.5px;line-height:10.5px;text-decoration:none;white-space:nowrap}
.quick-links a:nth-child(1){width:93px}
.quick-links a:nth-child(2){width:91px}
.quick-links a:nth-child(3){width:106px}
.tab-col{position:absolute;top:89px;height:636px;width:60px;text-align:center;color:var(--white);font-size:11px;font-weight:600;line-height:12.5px;letter-spacing:.5px}
.tab-col svg{display:block;margin:31px auto 6px}
.tab-apps{left:70px;background:var(--blue)}
.tab-videos{left:132px;background:var(--green)}
.panel{position:absolute;left:192px;top:89px;width:937px;height:636px;background:var(--red);color:var(--white)}
.share-bar{position:absolute;right:0;top:0;width:180px;height:36px;background:#160404;display:flex;align-items:center;padding-left:13px;gap:3px}
.share-btn{height:14px;padding:0 5px;background:#e8eef5;border:1px solid #b9c6d6;color:#3b5a88;font-size:8px;line-height:12px;border-radius:2px}
.share-count{height:14px;padding:0 5px;background:#fff;border:1px solid #ccc;color:#555;font-size:8px;line-height:12px;margin-right:4px}
.panel h1{position:absolute;left:34px;top:25px;font-size:37px;font-weight:600;letter-spacing:.3px}
.panel .intro{position:absolute;left:34px;top:77px;width:885px;font-size:12.5px;line-height:14.6px}
.tile{position:absolute;width:207px;height:219px}
.photo-desk{background:linear-gradient(160deg,#6d6257 0%,#3b3631 45%,#8a8378 75%,#5d7a3a 100%)}
.photo-portrait{background:linear-gradient(120deg,#9a8f82 0%,#3a332e 40%,#15151a 70%,#5b5650 100%)}
.tile-active{background:linear-gradient(150deg,#262322,#141313);text-align:center}
.tile-active .url{position:absolute;top:81px;width:100%;font-size:12.5px}
.tile-active .btns{position:absolute;top:113px;left:33px;display:flex;gap:2px}
.tile-active .btns span{display:block;width:64px;height:21px;line-height:21px;font-size:10.5px}
.btn-post{background:var(--post-blue)}
.btn-chirp{background:var(--chirp-blue)}
.tile-active svg{position:absolute;left:88px;top:149px}
.settings{position:absolute;right:9px;bottom:10px}
.footer{position:absolute;left:70px;top:735px;width:1059px;height:29px;background:var(--grey);color:var(--white);font-size:10.5px;line-height:29px;padding:0 14px;display:flex;justify-content:space-between}
</style>
</head>
<body>
<div class="canvas">
  <div class="brand">Noticely.me</div>
  <nav class="main-nav">
    <a class="nav-home" href="#">MY HOME PAGE</a>
    <a class="nav-videos" href="#">MY FAVORTES VIDEOS</a>
    <a class="nav-apps" href="#">PERSONAL APPS</a>
  </nav>
  <div class="top-links">
    <span class="dot"></span><span class="dot"></span>
    <svg width="11" height="11" viewBox="0 0 11 11"><circle cx="4.5" cy="4.5" r="3.3" fill="none" stroke="#9a9a9a" stroke-width="1.5"/><line x1="7" y1="7" x2="10.2" y2="10.2" stroke="#9a9a9a" stroke-width="1.8"/></svg>
    <span>Signin</span><span>Signup</span>
  </div>
  <div class="quick-links">
    <a href="#">Admin<br>Fevorites Videos</a>
    <a href="#">Talias Pics +<br>Favorites Links</a>
    <a href="#">Famiily Weekly<br>Calendar and Notes</a>
  </div>

  <div class="tab-col tab-apps">
    <svg width="36" height="36" viewBox="0 0 36 36"><circle cx="18" cy="18" r="15.5" fill="none" stroke="#fff" stroke-width="3"/><path d="M16 13l5 5-5 5" fill="none" stroke="#fff" stroke-width="2.5"/></svg>
    Personal<br>Apps
  </div>
  <div class="tab-col tab-videos">
    <svg width="36" height="36" viewBox="0 0 36 36"><circle cx="18" cy="18" r="15.5" fill="none" stroke="#fff" stroke-width="3"/><path d="M16 13l5 5-5 5" fill="none" stroke="#fff" stroke-width="2.5"/></svg>
    My<br>Favortes<br>Videos
  </div>

  <section class="panel">
    <div class="share-bar">
      <span class="share-btn">Chirp</span><span class="share-count">152</span>
      <span class="share-btn">Like</span><span class="share-count">52</span>
    </div>
    <h1>My Home Page</h1>
    <p class="intro">Lorem ipsum dolor sit amet, consectetur adipiscing elit. In fermentum dolor non augue pretium egestas. Donec sem eros, tincidunt at congue ut, posuere sit amet est. Vivamus scelerisque viverra odio sit amet laoreet. Ut nec neque non justo rutrum tempor lobortis eu ante. Aliquam sagittis, nibh quis commodo auctor, risus mauris laoreet lectus, id facilisis libero odio nec enim. Sed id ligula adipiscing purus lacinia aliquet</p>

    <div class="tile photo-desk" style="left:37px;top:140px" role="img" aria-label="Photo of two women working on laptops outdoors"></div>
    <div class="tile tile-active" style="left:256px;top:140px">
      <div class="url">www.samplecorner.net</div>
      <div class="btns"><span class="btn-post">Postwall</span><span class="btn-chirp">Chirper</span></div>
      <svg width="30" height="30" viewBox="0 0 30 30"><circle cx="15" cy="12" r="11" fill="#9b140a" stroke="#d33" stroke-width="1.5"/><path d="M13.5 8.5l3.5 3.5-3.5 3.5" fill="none" stroke="#fff" stroke-width="2"/></svg>
    </div>
    <div class="tile photo-desk" style="left:476px;top:140px" role="img" aria-label="Photo of two women working on laptops outdoors"></div>
    <div class="tile photo-portrait" style="left:695px;top:140px" role="img" aria-label="Portrait photo of business people"></div>

    <div class="tile photo-desk" style="left:37px;top:372px" role="img" aria-label="Photo of two women working on laptops outdoors"></div>
    <div class="tile photo-portrait" style="left:256px;top:372px" role="img" aria-label="Portrait photo of business people"></div>
    <div class="tile photo-desk" style="left:476px;top:372px" role="img" aria-label="Photo of two women working on laptops outdoors"></div>
    <div class="tile photo-portrait" style="left:695px;top:372px" role="img" aria-label="Portrait photo of business people"></div>

    <svg class="settings" width="19" height="19" viewBox="0 0 19 19"><circle cx="9.5" cy="9.5" r="9.5" fill="#3b7fc4"/><circle cx="9.5" cy="9.5" r="4.2" fill="none" stroke="#fff" stroke-width="2.2" stroke-dasharray="2 1.3"/><circle cx="9.5" cy="9.5" r="1.5" fill="#fff"/></svg>
  </section>

  <footer class="footer">
    <span>All Right Reserved © 2014&nbsp; With Noticely</span>
    <span>Terns and Conditions</span>
  </footer>
</div>
</body>
</html>
```